Velorak app icon design

We are building an Velorak app and would like some good looking icons to replace the boring ones we have created ourselves.

Please see attached screen shots.

The icons toggle "Active/Inactive" where the inactive is shaded out.

Building

```html
<!DOCTYPE html>
<html lang="en">
<head>
<meta charset="utf-8">
<title>Velorak app icon design</title>
<link href="https://fonts.googleapis.com/css2?family=Arimo:wght@400;700&family=Lato:wght@300&display=swap" rel="stylesheet">
<style>
:root{
  --bg:#1d3656;
  --screen:#ffffff;
  --bar:#f7f7f7;
  --line:#dcdcdc;
  --text:#1a1a1a;
  --muted:#8a8a8a;
  --icon:#8e8e8e;
  --ring:#a3a3a3;
  --disc:#f3f3f3;
  --blue:#1a7cf4;
  --field:#e3e3e6;
  --kbd:#d2d5db;
  --key:#ffffff;
  --key-dark:#adb3bc;
  --strip:#f1f1f1;
  --label:#ffffff;
  --battery:#4cd964;
}
*{box-sizing:border-box;margin:0;padding:0}
html,body{width:1200px;height:1200px;overflow:hidden}
body{background:var(--bg);position:relative;font-family:"Arimo",Arial,sans-serif;color:var(--text)}
.sprites{position:absolute;width:0;height:0}
.screen{position:absolute;top:152px;width:307px;height:538px;background:var(--screen);overflow:hidden}
.screen--filtered{left:37px}
.screen--typing{left:431px;top:146px}
.screen--results{left:827px}
.status-bar{height:22px;display:flex;align-items:center;justify-content:space-between;padding:0 8px;font-size:10.5px;font-weight:700;background:var(--bar)}
.status-bar .carrier{display:flex;align-items:center;gap:4px}
.signal{letter-spacing:-1px;font-size:9px}
.battery{width:20px;height:9px;border:1px solid #555;border-radius:2px;padding:1px;position:relative}
.battery::before{content:"";display:block;height:100%;width:75%;background:var(--battery)}
.nav-bar{height:40px;position:relative;display:flex;align-items:center;justify-content:center;background:var(--bar);font-size:18px}
.nav-back{position:absolute;left:10px;color:var(--blue);font-size:13px;display:flex;align-items:center;gap:4px}
.nav-back svg{width:9px;height:14px}
.filter-row{height:60px;display:flex;justify-content:space-around;align-items:flex-start;padding:2px 6px 0;background:var(--bar);border-bottom:1px solid var(--line)}
.filter{display:flex;flex-direction:column;align-items:center;width:48px}
.filter svg{width:34px;height:34px}
.filter span{font-size:7.5px;color:var(--muted);margin-top:1px}
.filter.is-inactive{opacity:.3}
.search-area{height:38px;padding:6px 8px;background:var(--bar);border-bottom:1px solid var(--line)}
.search-field{height:26px;border-radius:5px;background:var(--field);display:flex;align-items:center;gap:6px;padding:0 8px;font-size:12px}
.search-field svg{width:11px;height:11px}
.search-field.is-empty{color:var(--muted)}
.result{height:44px;display:flex;align-items:center;gap:8px;padding:0 8px;border-bottom:1px solid var(--line);font-size:12px;line-height:1.2}
.result svg{width:30px;height:30px;flex:none}
.keyboard{position:absolute;left:0;right:0;bottom:0;height:203px;background:var(--kbd);padding:10px 3px 4px;display:flex;flex-direction:column;gap:12px}
.key-row{display:flex;justify-content:center;gap:4px}
.key{width:26px;height:33px;background:var(--key);border-radius:4px;box-shadow:0 1px 0 #8d9096;display:flex;align-items:center;justify-content:center;font-size:18px}
.key--dark{background:var(--key-dark)}
.key--wide{width:36px}
.key--mode{width:70px;font-size:13px}
.key--space{width:146px;font-size:13px}
.key--return{width:70px;font-size:13px}
.key-row--bottom{justify-content:space-between;padding:0 2px}
.icon-strip{position:absolute;background:var(--strip)}
.icon-strip--active{left:11px;top:843px;width:685px;height:108px;display:flex}
.strip-cell{flex:1;display:flex;flex-direction:column;align-items:center;padding-top:8px}
.strip-cell svg{width:72px;height:72px}
.strip-cell span{font-size:15px;color:var(--muted);margin-top:-2px}
.strip-cell--all{border-left:1px solid var(--line)}
.icon-strip--inactive{left:0;top:1040px;width:697px;height:104px}
.icon-strip--inactive svg{position:absolute;top:20px;width:66px;height:66px;opacity:.22}
.strip-title{position:absolute;left:727px;color:var(--label);font-family:"Lato",Arial,sans-serif;font-weight:300;font-size:50px}
.strip-title--active{top:868px}
.strip-title--inactive{top:1064px}
</style>
</head>
<body>

<svg class="sprites" aria-hidden="true">
  <defs>
    <symbol id="ic-folder" viewBox="0 0 40 40"><circle cx="20" cy="20" r="18.5" fill="var(--disc)" stroke="var(--ring)" stroke-width="1.2"/><path d="M9 13h8l2 2h12v14H9z" fill="var(--icon)"/></symbol>
    <symbol id="ic-house" viewBox="0 0 40 40"><circle cx="20" cy="20" r="18.5" fill="var(--disc)" stroke="var(--ring)" stroke-width="1.2"/><path d="M20 8 7.5 20H11v11h6v-7h6v7h6V20h3.5z" fill="var(--icon)"/></symbol>
    <symbol id="ic-clipboard" viewBox="0 0 40 40"><circle cx="20" cy="20" r="18.5" fill="var(--disc)" stroke="var(--ring)" stroke-width="1.2"/><rect x="12" y="11" width="16" height="20" rx="2" fill="var(--icon)"/><rect x="16" y="9" width="8" height="4" rx="1" fill="var(--icon)" stroke="var(--disc)" stroke-width="1"/></symbol>
    <symbol id="ic-person" viewBox="0 0 40 40"><circle cx="20" cy="20" r="18.5" fill="var(--disc)" stroke="var(--ring)" stroke-width="1.2"/><circle cx="20" cy="15" r="6" fill="var(--icon)"/><path d="M8.5 33c0-8 5-11 11.5-11s11.5 3 11.5 11z" fill="var(--icon)"/></symbol>
    <symbol id="ic-owner" viewBox="0 0 40 40"><circle cx="20" cy="20" r="18.5" fill="var(--disc)" stroke="var(--ring)" stroke-width="1.2"/><circle cx="20" cy="15" r="6" fill="var(--icon)"/><path d="M8.5 33c0-8 5-11 11.5-11s11.5 3 11.5 11z" fill="var(--icon)"/><path d="M18.8 22h2.4l-.5 6-.7 2-.7-2z" fill="var(--disc)"/></symbol>
    <symbol id="ic-staff" viewBox="0 0 40 40"><circle cx="20" cy="20" r="18.5" fill="var(--disc)" stroke="var(--ring)" stroke-width="1.2"/><circle cx="24" cy="14" r="5" fill="var(--icon)"/><path d="M15 30c0-6 4-9 9-9s9 3 9 9z" fill="var(--icon)"/><circle cx="16" cy="17" r="5" fill="var(--icon)" stroke="var(--disc)" stroke-width="1"/><path d="M7 33c0-6 4-9 9-9s9 3 9 9z" fill="var(--icon)" stroke="var(--disc)" stroke-width="1"/></symbol>
    <symbol id="ic-search" viewBox="0 0 12 12"><circle cx="5" cy="5" r="3.6" fill="none" stroke="#7d7d7d" stroke-width="1.4"/><path d="m7.6 7.6 3 3" stroke="#7d7d7d" stroke-width="1.4"/></symbol>
    <symbol id="ic-back" viewBox="0 0 9 14"><path d="M7.5 1 1.5 7l6 6" fill="none" stroke="var(--blue)" stroke-width="2"/></symbol>
  </defs>
</svg>

<!-- Screen: search filtered by Owner off -->
<section class="screen screen--filtered">
  <div class="status-bar"><span class="carrier"><span class="signal">●●●●○</span>NORTHCELL</span><span>9:26 PM</span><span class="battery"></span></div>
  <div class="nav-bar"><span class="nav-back"><svg><use href="#ic-back"/></svg>Home</span>Search</div>
  <div class="filter-row">
    <div class="filter"><svg><use href="#ic-folder"/></svg><span>All</span></div>
    <div class="filter"><svg><use href="#ic-house"/></svg><span>Property</span></div>
    <div class="filter is-inactive"><svg><use href="#ic-owner"/></svg><span>Owner</span></div>
    <div class="filter"><svg><use href="#ic-person"/></svg><span>Tanant</span></div>
    <div class="filter"><svg><use href="#ic-staff"/></svg><span>Staff</span></div>
  </div>
  <div class="search-area"><div class="search-field"><svg><use href="#ic-search"/></svg>Main</div></div>
  <div class="result"><svg><use href="#ic-house"/></svg><p>2/19 Corvan St<br>Harlow East Nsw 2401</p></div>
  <div class="result"><svg><use href="#ic-house"/></svg><p>8/109 Pellow Street<br>Harlow East Nsw 2401</p></div>
  <div class="result"><svg><use href="#ic-house"/></svg><p>Domain 604/22 Sir Elric Vane<br>Cresent</p></div>
  <div class="result"><svg><use href="#ic-house"/></svg><p>8/913 Tenby Street<br>Harlow Est 2401</p></div>
  <div class="result"><svg><use href="#ic-house"/></svg><p>2/91 Marsh Street<br>Harlow East Nsw 2401</p></div>
  <div class="result"><svg><use href="#ic-person"/></svg><p>KTR Building Maintanance &amp;<br>Electrical Service P/L</p></div>
  <div class="result"><svg><use href="#ic-person"/></svg><p>Ranjit, Devan Pal</p></div>
  <div class="result"><svg><use href="#ic-person"/></svg><p>Osei Linal, Marta</p></div>
</section>

<!-- Screen: empty search with keyboard -->
<section class="screen screen--typing">
  <div class="status-bar"><span class="carrier"><span class="signal">●●●●○</span>NORTHCELL</span><span>9:26 PM</span><span class="battery"></span></div>
  <div class="nav-bar">Search</div>
  <div class="filter-row">
    <div class="filter"><svg><use href="#ic-clipboard"/></svg><span>My Portfolio</span></div>
    <div class="filter"><svg><use href="#ic-house"/></svg><span>Property</span></div>
    <div class="filter"><svg><use href="#ic-owner"/></svg><span>Owner</span></div>
    <div class="filter"><svg><use href="#ic-person"/></svg><span>Tanant</span></div>
    <div class="filter"><svg><use href="#ic-staff"/></svg><span>Staff</span></div>
  </div>
  <div class="search-area"><div class="search-field is-empty"><svg><use href="#ic-search"/></svg>Search</div></div>
  <div class="keyboard">
    <div class="key-row"><span class="key">Q</span><span class="key">W</span><span class="key">E</span><span class="key">R</span><span class="key">T</span><span class="key">Y</span><span class="key">U</span><span class="key">I</span><span class="key">O</span><span class="key">P</span></div>
    <div class="key-row"><span class="key">A</span><span class="key">S</span><span class="key">D</span><span class="key">F</span><span class="key">G</span><span class="key">H</span><span class="key">J</span><span class="key">K</span><span class="key">L</span></div>
    <div class="key-row"><span class="key key--dark key--wide">⇧</span><span class="key">Z</span><span class="key">X</span><span class="key">C</span><span class="key">V</span><span class="key">B</span><span class="key">N</span><span class="key">M</span><span class="key key--dark key--wide">⌫</span></div>
    <div class="key-row key-row--bottom"><span class="key key--dark key--mode">.?123</span><span class="key key--space">space</span><span class="key key--dark key--return">return</span></div>
  </div>
</section>

<!-- Screen: all results -->
<section class="screen screen--results">
  <div class="status-bar"><span class="carrier"><span class="signal">●●●●○</span>NORTHCELL</span><span>9:26 PM</span><span class="battery"></span></div>
  <div class="nav-bar"><span class="nav-back"><svg><use href="#ic-back"/></svg>Home</span>Search</div>
  <div class="filter-row">
    <div class="filter"><svg><use href="#ic-folder"/></svg><span>All</span></div>
    <div class="filter"><svg><use href="#ic-house"/></svg><span>Property</span></div>
    <div class="filter"><svg><use href="#ic-owner"/></svg><span>Owner</span></div>
    <div class="filter"><svg><use href="#ic-person"/></svg><span>Tanant</span></div>
    <div class="filter"><svg><use href="#ic-staff"/></svg><span>Staff</span></div>
  </div>
  <div class="search-area"><div class="search-field"><svg><use href="#ic-search"/></svg>Main</div></div>
  <div class="result"><svg><use href="#ic-house"/></svg><p>2/19 Corvan St<br>Harlow East Nsw 2401</p></div>
  <div class="result"><svg><use href="#ic-house"/></svg><p>8/109 Pellow Street<br>Harlow East Nsw 2401</p></div>
  <div class="result"><svg><use href="#ic-house"/></svg><p>Domain 604/22 Sir Elric Vane<br>Cresent</p></div>
  <div class="result"><svg><use href="#ic-owner"/></svg><p>Clara Whitfield for Truestees For Elm<br>Maintanance Tr</p></div>
  <div class="result"><svg><use href="#ic-owner"/></svg><p>Clara Whitfield Trustees for Elm<br>Maintanance Tr</p></div>
  <div class="result"><svg><use href="#ic-person"/></svg><p>KTR Building Maintanance &amp;<br>Electrical Service P/L</p></div>
  <div class="result"><svg><use href="#ic-person"/></svg><p>Ranjit, Devan Pal</p></div>
  <div class="result"><svg><use href="#ic-person"/></svg><p>Osei Linal, Marta</p></div>
</section>

<!-- Icon set: active -->
<div class="icon-strip icon-strip--active">
  <div class="strip-cell"><svg><use href="#ic-clipboard"/></svg><span>My Portfolio</span></div>
  <div class="strip-cell"><svg><use href="#ic-house"/></svg><span>Property</span></div>
  <div class="strip-cell"><svg><use href="#ic-owner"/></svg><span>Owner</span></div>
  <div class="strip-cell"><svg><use href="#ic-person"/></svg><span>Tanant</span></div>
  <div class="strip-cell"><svg><use href="#ic-staff"/></svg><span>Staff</span></div>
  <div class="strip-cell strip-cell--all"><svg><use href="#ic-folder"/></svg><span>All</span></div>
</div>
<h2 class="strip-title strip-title--active">Active Icons</h2>

<!-- Icon set: inactive -->
<div class="icon-strip icon-strip--inactive">
  <svg style="left:57px"><use href="#ic-folder"/></svg>
  <svg style="left:150px"><use href="#ic-house"/></svg>
  <svg style="left:237px"><use href="#ic-clipboard"/></svg>
  <svg style="left:314px"><use href="#ic-staff"/></svg>
  <svg style="left:417px"><use href="#ic-person"/></svg>
  <svg style="left:513px"><use href="#ic-owner"/></svg>
  <svg style="left:614px"><use href="#ic-clipboard"/></svg>
</div>
<h2 class="strip-title strip-title--inactive">Inactive Icons</h2>

</body>
</html>
```